We need a web site design that is connected to Ridgeway Roofing an American company, Veteran owned. Specializing in new roofs of all kinds, repair existing roofs and emergency roof repairs. located in the north Georgia mountains

Target Market(s)

homeowners end users, real estate, home owners insurance companies

Industry/Entity Type

roofing

Contact Information for Business Card

logo, Veteran owned, supports veteran charities, phone number ect

Font styles to use
Serif

Requirements
Should not have
• na

```html
<!DOCTYPE html>
<html lang="en">
<head>
<meta charset="utf-8">
<title>Ridgeway Roofing — Business Card</title>
<link rel="stylesheet" href="https://fonts.googleapis.com/css2?family=Lora:wght@400;600;700&display=swap">
<style>
  :root {
    --page: #ecebe8;
    --card: #ffffff;
    --brand-red: #d9301a;
    --ink: #111111;
    --ink-soft: #2a2a2a;
    --rule: #3a3a3a;
    --gold-light: #f3dc9a;
    --gold-mid: #e8c46a;
    --gold-deep: #c98a12;
  }
  * { box-sizing: border-box; margin: 0; padding: 0; }
  html, body {
    width: 1189px; height: 1200px; overflow: hidden;
    background: var(--page);
    font-family: "Lora", Georgia, serif;
  }
  .canvas { position: relative; width: 1189px; height: 1200px; }
  .card {
    position: absolute; left: 169px; width: 851px; height: 485px;
    background: var(--card); border-radius: 33px; overflow: hidden;
    box-shadow: 0 6px 16px rgba(0,0,0,0.18);
  }
  .card--front { top: 112px; }
  .card--back { top: 641px; }

  .brand-block {
    position: absolute; display: flex; flex-direction: column; align-items: center;
    transform: translate(-50%, -50%); white-space: nowrap;
  }
  .wordmark {
    display: flex; align-items: center; gap: 14px;
    color: var(--brand-red); font-weight: 700;
  }
  .wordmark__dot { border-radius: 50%; background: var(--brand-red); flex: none; }
  .tagline {
    color: var(--ink-soft); font-weight: 400; letter-spacing: 2px; text-transform: uppercase;
  }
  .tagline__sep { display: inline-block; width: 28px; height: 2px; background: var(--gold-deep); vertical-align: middle; margin: 0 12px; }

  .card--front .brand-block { left: 50%; top: 50%; }
  .card--front .wordmark { font-size: 46px; }
  .card--front .wordmark__dot { width: 30px; height: 30px; }
  .card--front .tagline { font-size: 15px; margin-top: 14px; }

  .card--back .brand-block { left: 231px; top: 242px; }
  .card--back .wordmark { font-size: 29px; gap: 10px; }
  .card--back .wordmark__dot { width: 20px; height: 20px; }
  .card--back .tagline { font-size: 12px; margin-top: 8px; letter-spacing: 1.5px; }

  .divider {
    position: absolute; left: 409px; top: 147px; width: 2px; height: 192px;
    background: var(--rule);
  }
  .contact { position: absolute; left: 461px; top: 140px; }
  .contact__name { font-size: 30px; font-weight: 700; color: var(--ink); line-height: 1.2; }
  .contact__role { font-size: 17px; color: var(--ink-soft); margin-top: 2px; }
  .contact__rule { width: 65px; height: 3px; background: var(--brand-red); margin: 14px 0 22px; }
  .contact__list { list-style: none; }
  .contact__item {
    display: flex; align-items: center; gap: 14px;
    font-size: 21px; color: var(--ink-soft); height: 29px;
  }
  .contact__icon {
    width: 24px; height: 24px; border-radius: 50%; background: var(--brand-red);
    display: flex; align-items: center; justify-content: center; flex: none;
  }
  .address-band {
    position: absolute; left: 0; right: 0; top: 410px; height: 41px;
    background: linear-gradient(to bottom, var(--gold-light) 0%, var(--gold-mid) 60%, var(--gold-deep) 100%);
    display: flex; align-items: center; justify-content: center;
    font-size: 19px; letter-spacing: 2px; color: var(--ink);
  }
</style>
</head>
<body>
<main class="canvas">
  <section class="card card--front" aria-label="Card front">
    <div class="brand-block">
      <div class="wordmark"><span class="wordmark__dot"></span>Ridgeway Roofing</div>
      <div class="tagline">Veteran Owned<span class="tagline__sep"></span>Supporting Veteran Charities</div>
    </div>
  </section>

  <section class="card card--back" aria-label="Card back">
    <div class="brand-block">
      <div class="wordmark"><span class="wordmark__dot"></span>Ridgeway Roofing</div>
      <div class="tagline">Veteran Owned &amp; Operated</div>
    </div>
    <div class="divider"></div>
    <div class="contact">
      <div class="contact__name">Daniel R Carter</div>
      <div class="contact__role">CEO</div>
      <div class="contact__rule"></div>
      <ul class="contact__list">
        <li class="contact__item">
          <span class="contact__icon">
            <svg width="14" height="14" viewBox="0 0 24 24"><path fill="#fff" d="M6.6 10.8a15.1 15.1 0 0 0 6.6 6.6l2.2-2.2a1 1 0 0 1 1-.25 11.4 11.4 0 0 0 3.6.57 1 1 0 0 1 1 1V20a1 1 0 0 1-1 1A17 17 0 0 1 3 4a1 1 0 0 1 1-1h3.5a1 1 0 0 1 1 1c0 1.25.2 2.45.57 3.57a1 1 0 0 1-.25 1z"/></svg>
          </span>(706) 555-0148
        </li>
        <li class="contact__item">
          <span class="contact__icon">
            <svg width="14" height="14" viewBox="0 0 24 24"><rect x="2" y="5" width="20" height="14" rx="1" fill="#fff"/><path d="M2 6l10 7 10-7" fill="none" stroke="#d9301a" stroke-width="2"/></svg>
          </span>hello@ridgewayroofs.com
        </li>
        <li class="contact__item">
          <span class="contact__icon">
            <svg width="14" height="14" viewBox="0 0 24 24" fill="none" stroke="#fff" stroke-width="2"><circle cx="12" cy="12" r="9"/><path d="M3 12h18M12 3c3 3 3 15 0 18M12 3c-3 3-3 15 0 18"/></svg>
          </span>www.ridgewayroofs.com
        </li>
      </ul>
    </div>
    <div class="address-band">418 Laurel Ridge Rd Ste 12, Blue Ridge, GA 30513</div>
  </section>
</main>
</body>
</html>
```